Ledger Ready Business Card

I need a business card designed around my logo (which was designed here on Sketch Yard!)

Target Market(s)

Professional Businesses

Industry/Entity Type

Business

Requirements
Must have
• Details that must be on the business card:

Harriet Vantos
Director
0491 263 358
harriet@ledgerready.com.au
www.ledgerready.com.au
PO Box 4471 Harrow Vale Vic 3921

```html
<!DOCTYPE html>
<html lang="en">
<head>
<meta charset="utf-8">
<title>Ledger Ready Business Card</title>
<link rel="stylesheet" href="https://fonts.googleapis.com/css2?family=PT+Sans:wght@400;700&display=swap">
<style>
  :root {
    --backdrop: #222223;
    --card: #ffffff;
    --ink: #1c1c1c;
    --brand-red: #d1232a;
  }
  * { margin: 0; padding: 0; box-sizing: border-box; }
  html, body {
    width: 1200px; height: 900px; overflow: hidden;
    background: var(--backdrop);
    font-family: "PT Sans", sans-serif;
  }
  .stage { position: relative; width: 1200px; height: 900px; }
  .card {
    position: absolute; top: 305px;
    width: 500px; height: 290px;
    background: var(--card);
    border-radius: 26px;
    overflow: hidden;
  }
  .card--front { left: 70px; }
  .card--back { left: 630px; }
  .card__stripes { position: absolute; inset: 0; width: 500px; height: 290px; }
  .card__stripes line { stroke: var(--brand-red); stroke-width: 12; }
  .wordmark {
    position: absolute; display: flex; align-items: center; gap: 12px;
    color: var(--ink); font-weight: 400; text-transform: uppercase;
    letter-spacing: 0.5px; white-space: nowrap;
  }
  .wordmark__mark { width: 30px; height: 30px; background: var(--brand-red); }
  .card--front .wordmark { left: 110px; top: 124px; font-size: 34px; }
  .card--front .wordmark__mark { width: 36px; height: 36px; }
  .card--back .wordmark { left: 92px; top: 64px; font-size: 27px; }
  .contact {
    position: absolute; left: 148px; top: 150px;
    color: var(--ink); font-size: 14px; line-height: 1.25;
  }
  .contact__name { color: var(--brand-red); font-size: 20px; line-height: 1.1; }
  .contact__role { font-size: 13px; margin-bottom: 16px; }
  .contact__address { margin-bottom: 10px; }
  .contact__sep { color: var(--brand-red); font-weight: 700; padding: 0 3px; }
</style>
</head>
<body>
<main class="stage">
  <section class="card card--front" aria-label="Card front">
    <svg class="card__stripes" viewBox="0 0 500 290" aria-hidden="true">
      <line x1="330" y1="-10" x2="515" y2="166"/>
      <line x1="372" y1="-10" x2="515" y2="126"/>
    </svg>
    <div class="wordmark"><span class="wordmark__mark"></span>Ledger Ready</div>
  </section>

  <section class="card card--back" aria-label="Card back">
    <svg class="card__stripes" viewBox="0 0 500 290" aria-hidden="true">
      <line x1="-8" y1="92" x2="96" y2="300"/>
      <line x1="-8" y1="150" x2="67" y2="300"/>
    </svg>
    <div class="wordmark"><span class="wordmark__mark"></span>Ledger Ready</div>
    <div class="contact">
      <p class="contact__name">Harriet Vantos</p>
      <p class="contact__role">Director</p>
      <p class="contact__address">PO Box 4471 Harrow Vale Vic 3921</p>
      <p>0491 263 358<span class="contact__sep">|</span>harriet@ledgerready.com.au</p>
      <p>www.ledgerready.com.au</p>
    </div>
  </section>
</main>
</body>
</html>
```